General Contractor/ Real Estate Family Business AMAZING Drywall/Paint Flyer

We need to have a flyer designed to market our drywall repair services. We are looking to increase our business in this field and plan on using this flyer in both print and as an eflyer to use in email marketing campaigns. We would like to incorporate past flyer designs and colors/ logos into this flyer so our marketing stays consistent.

Target Market(s)

Drywall repair, Insurance Restoration, Real Estate Agents, Property Managers, Real Estate Investors, Single family residential homeowners.

Industry/Entity Type

Real Estate

Font styles to use
Sans Serif

Requirements
Must have
• Must include the logos provided, pictures provided, and incorporate the copy provided in the attached word document. Must include our license number. Must be able to fit a standard 8.5"x11" flyer size. Must also be optimized to use online as an eflyer in online marketing campaigns.
Nice to have
• It would be nice to incorporate some of the designs and colors form previous flyers to keep our marketing consistent. Past flyers are attached in the documents.

```html
<!DOCTYPE html>
<html lang="en">
<head>
<meta charset="utf-8">
<title>Castellan Property Solutions – Drywall &amp; Paint Flyer</title>
<link href="https://fonts.googleapis.com/css2?family=Bebas+Neue&family=Open+Sans:wght@400;600;700&display=swap" rel="stylesheet">
<style>
  :root{
    --blue:#416aad;
    --orange:#c67e50;
    --grey:#e6e7e9;
    --ink:#333538;
    --white:#ffffff;
    --page:#b3b3b3;
  }
  *{margin:0;padding:0;box-sizing:border-box}
  html,body{width:917px;height:1200px;overflow:hidden;background:var(--page)}
  .stage{position:relative;width:917px;height:1200px}
  .flyer{
    position:absolute;left:34.5px;top:0;
    width:913px;height:1292px;
    transform:scale(0.92879);transform-origin:0 0;
    background:var(--white);overflow:hidden;
    font-family:"Open Sans",Arial,sans-serif;
  }
  .hero-photo{position:absolute;left:0;top:0;width:913px;height:660px;
    background:
      linear-gradient(180deg,#f1ece4 0%,#e4dccd 18%,transparent 30%),
      linear-gradient(180deg,transparent 30%,#3b2a20 32%,#3a2a20 58%,#c9b79c 60%,#d9c9ae 100%);
  }
  .hero-shapes{position:absolute;left:0;top:0}
  .brand{position:absolute;left:60px;top:0;width:175px;height:147px;
    background:var(--white);border-radius:0 0 14px 14px;
    display:flex;align-items:center;justify-content:center;text-align:center;
    color:var(--blue);font-weight:700;font-size:14px;line-height:1.3;padding:0 8px;white-space:nowrap}
  .headline{position:absolute;left:0;top:570px;width:913px;text-align:center;
    font-family:"Bebas Neue","Arial Narrow",sans-serif;color:var(--blue);font-weight:400}
  .headline-line{display:block;font-size:55px;line-height:56px;
    transform:scaleX(0.84);transform-origin:50% 50%;white-space:nowrap}
  .services{position:absolute;left:72px;top:718px;width:770px;
    display:grid;grid-template-columns:244px 244px 244px;column-gap:19px;row-gap:20px}
  .service{height:80px;border-radius:14px;color:var(--white);
    display:flex;align-items:center;justify-content:center;text-align:center;
    font-weight:600;font-size:16.5px;line-height:20px;padding:0 10px}
  .service--orange{background:var(--orange)}
  .service--blue{background:var(--blue)}
  .about{position:absolute;left:0;top:950px;width:913px;height:230px;background:var(--grey)}
  .about-col{position:absolute;top:52px;width:370px;font-size:15px;line-height:19px;color:var(--ink)}
  .about-col p+p{margin-top:22px}
  .about-col--left{left:58px;text-align:right}
  .about-col--right{left:483px}
  .about-divider{position:absolute;left:456px;top:38px;width:2px;height:164px;background:var(--blue)}
  .contact{position:absolute;left:0;top:1180px;width:913px;height:112px;background:var(--orange);color:var(--white);font-weight:700;font-size:18.5px;line-height:25px}
  .contact-cta{position:absolute;right:483px;top:21px;text-align:right;width:360px}
  .contact-info{position:absolute;left:473px;top:21px}
</style>
</head>
<body>
<div class="stage">
  <div class="flyer">
    <div class="hero-photo" role="img" aria-label="Photo of a finished kitchen with dark wood cabinets, stainless microwave and track lighting"></div>
    <svg class="hero-shapes" width="913" height="1292" viewBox="0 0 913 1292" aria-hidden="true">
      <path d="M0,440 C250,360 650,355 913,522" fill="none" stroke="#fff" stroke-width="8"/>
      <path d="M0,440 C250,360 650,355 913,522 L913,1292 L0,1292 Z" fill="var(--blue)"/>
      <path d="M0,600 C180,510 400,470 600,475 C760,480 880,540 913,560 L913,1292 L0,1292 Z" fill="#fff"/>
      <path d="M300,497 C520,465 760,480 913,533" fill="none" stroke="#fff" stroke-width="8"/>
      <path d="M300,497 C520,465 760,480 913,533 L913,645 C820,540 620,485 300,497 Z" fill="var(--orange)"/>
    </svg>
    <div class="brand">Castellan<br>Property Solutions, LLC</div>

    <h1 class="headline">
      <span class="headline-line">Top Quality Drywall Repair, Installation,</span>
      <span class="headline-line">Painting &amp; Insurance Restoration Services!</span>
    </h1>

    <div class="services">
      <div class="service service--orange">Drywall Repair and<br>Hole Patching</div>
      <div class="service service--blue">Drywall Repair and<br>Hole Patching</div>
      <div class="service service--orange">Popcorn Ceiling<br>Removal</div>
      <div class="service service--blue">All Textures- Orange Peel,<br>Knockdown, Smooth<br>Finish, Skip Trowel</div>
      <div class="service service--orange">Complete Interior and<br>Exterior Painting</div>
      <div class="service service--blue">Insurance Restoration-<br>Fire, Water Damage</div>
    </div>

    <section class="about">
      <div class="about-col about-col--left">
        <p>Castellan Property Solutions LLC has 10+ years’<br>experience here in Maricopa County.</p>
        <p>We can handle your entire drywall, painting, or<br>restoration project- no need to hire multiple<br>companies or subs. Just bring us in and let us<br>give you a stress free one stop shop experience.</p>
      </div>
      <div class="about-divider"></div>
      <div class="about-col about-col--right">
        <p>Locally owned family business with an A+ QSB<br>rating, full general contractor license/insurance.</p>
        <p>Customers who work with us typically hire<br>us for our professional quality work that’s<br>always consistent, reliable, and<br>completed on deadline.</p>
      </div>
    </section>

    <footer class="contact">
      <div class="contact-cta">Contact us today to discuss your<br>project and receive a free estimate<br>within 72 hours!</div>
      <div class="contact-info">Phone (602) 555-0148<br>www.castellanpropertysolutions.com<br>solutions@castellanproperties.com</div>
    </footer>
  </div>
</div>
</body>
</html>
```